brake hoses

revamp current brake hose flyer - modernize make it look better

please use website
Kestrelmotorworks.co.nz for as much as possible

i want you all to come with own wording description etc

```html
<!DOCTYPE html>
<html lang="en">
<head>
<meta charset="utf-8">
<title>Brake Hoses &amp; Pipes Flyer – Kestrel Motorworks</title>
<link rel="stylesheet" href="https://fonts.googleapis.com/css2?family=Bebas+Neue&family=Poppins:ital,wght@0,400;0,500;0,600;1,400&display=swap">
<style>
  :root {
    --yellow: #f9d808;
    --yellow-deep: #f2c800;
    --black: #111111;
    --charcoal: #1f1f1f;
    --steel: #3a3a3a;
    --white: #ffffff;
    --paper: #f4f4f4;
    --grey-line: #d9d9d9;
    --text: #141414;
  }
  * { box-sizing: border-box; margin: 0; padding: 0; }
  html, body { width: 735px; height: 1200px; overflow: hidden; background: var(--white); }
  .flyer {
    position: relative; width: 735px; height: 1200px; overflow: hidden;
    font-family: "Poppins", sans-serif; color: var(--text);
  }
  .backdrop { position: absolute; inset: 0; }

  .headline {
    position: absolute; left: 85px; top: 52px;
    font-family: "Bebas Neue", sans-serif; color: var(--black);
    font-size: 136px; line-height: 0.86; letter-spacing: -1px;
  }
  .headline__tag {
    display: inline-block; margin-top: 10px;
    background: var(--black); color: var(--white);
    font-size: 92px; line-height: 1; padding: 2px 14px 0 14px;
    border-radius: 10px;
  }

  .brand {
    position: absolute; left: 377px; top: 180px; width: 300px;
    display: flex; flex-direction: column; align-items: center; gap: 16px;
  }
  .brand__dot { width: 58px; height: 58px; border-radius: 50%; background: var(--black); }
  .brand__name {
    font-weight: 600; font-size: 19px; color: var(--black);
    letter-spacing: 0.5px; text-align: center; white-space: nowrap;
  }

  .range {
    position: absolute; left: 513px; top: 350px;
    font-weight: 600; font-size: 25px; line-height: 1.25; color: var(--black);
  }
  .range::after {
    content: ""; display: block; width: 92px; height: 2px;
    background: var(--yellow); margin-top: 8px;
  }

  .product-photo {
    position: absolute; left: 72px; top: 438px; width: 606px; height: 270px;
    border-radius: 14px;
    background: radial-gradient(ellipse at 50% 55%, #d9d9d9 0%, #ececec 45%, #fafafa 80%);
  }

  .info-card {
    position: absolute; top: 742px; width: 300px; height: 320px;
    border: 1.5px solid var(--charcoal); border-radius: 18px;
    background: var(--white); overflow: hidden;
  }
  .info-card--about { left: 60px; }
  .info-card--services { left: 375px; padding: 22px 0 0 36px; }

  .about__top { padding: 20px 16px 0 34px; height: 160px; }
  .about__title {
    font-family: "Bebas Neue", sans-serif; font-size: 33px; line-height: 1;
    color: var(--black); white-space: nowrap;
  }
  .about__text { font-size: 17px; line-height: 1.3; margin-top: 8px; }
  .about__aim {
    position: absolute; left: 0; right: 0; bottom: 0; top: 162px;
    background: var(--yellow); border-top: 1.5px solid var(--charcoal);
    padding: 14px 20px 0 34px;
  }
  .about__aim-title {
    font-family: "Bebas Neue", sans-serif; font-size: 40px; line-height: 1; color: var(--black);
  }
  .about__aim-text { font-size: 17px; line-height: 1.3; margin-top: 6px; }
  .target-icon { position: absolute; left: 278px; top: 894px; width: 74px; height: 74px; }

  .services { list-style: none; display: grid; grid-template-columns: 108px 1fr; row-gap: 12px; }
  .services li {
    display: flex; align-items: flex-start; gap: 10px;
    font-size: 21px; line-height: 1.35;
  }
  .services li.wide { grid-column: 1 / 3; }
  .tick { flex: none; width: 21px; height: 21px; margin-top: 4px; }

  .contact {
    position: absolute; top: 1098px; list-style: none;
    color: var(--white); font-size: 15.5px; line-height: 1.72; white-space: nowrap;
  }
  .contact--left { left: 60px; }
  .contact--right { left: 418px; }
  .contact li { display: flex; align-items: center; gap: 12px; }
  .contact .icon { width: 19px; height: 19px; flex: none; }
  .contact .no-icon { padding-left: 31px; }
  .unsubscribe { color: var(--yellow); font-style: italic; font-size: 12.5px; padding-left: 31px; }
</style>
</head>
<body>
<main class="flyer">
  <svg class="backdrop" width="735" height="1200" viewBox="0 0 735 1200" aria-hidden="true">
    <defs>
      <linearGradient id="band" x1="0" y1="0" x2="1" y2="1">
        <stop offset="0" stop-color="#2c2c2c"/>
        <stop offset="0.5" stop-color="#1c1c1c"/>
        <stop offset="1" stop-color="#333333"/>
      </linearGradient>
      <linearGradient id="sun" x1="0" y1="0" x2="0" y2="1">
        <stop offset="0" stop-color="#fadd0a"/>
        <stop offset="1" stop-color="#f6d200"/>
      </linearGradient>
    </defs>
    <rect width="735" height="1200" fill="url(#sun)"/>
    <path d="M0,522 C170,420 420,340 735,336 L735,1200 L0,1200 Z" fill="#ffffff"/>
    <path d="M0,1024 C250,980 500,900 735,826 L735,860 C500,930 250,1008 0,1050 Z" fill="#e6e6e6"/>
    <path d="M0,1040 C250,1000 500,922 735,846 L735,1200 L0,1200 Z" fill="url(#band)"/>
  </svg>

  <h1 class="headline">BRAKE<br>HOSES<br><span class="headline__tag">&amp; PIPES</span></h1>

  <div class="brand">
    <span class="brand__dot"></span>
    <span class="brand__name">KESTREL MOTORWORKS</span>
  </div>

  <p class="range">Large range<br>of Hoses</p>

  <div class="product-photo" role="img" aria-label="Braided steel brake hoses, rubber brake hoses, bent metal pipe, mounting brackets and brass fittings"></div>

  <section class="info-card info-card--about">
    <div class="about__top">
      <h2 class="about__title">KESTREL MOTORWORKS</h2>
      <p class="about__text">Specialise in the<br>Manufacture of Rubber<br>&amp; Braided Hoses</p>
    </div>
    <div class="about__aim">
      <h3 class="about__aim-title">OUR AIM IS</h3>
      <p class="about__aim-text">to have parts repaired<br>with the quickest turn-<br>around times possible</p>
    </div>
  </section>

  <svg class="target-icon" viewBox="0 0 74 74" aria-hidden="true">
    <circle cx="37" cy="37" r="31" fill="var(--yellow)" stroke="#111" stroke-width="2.5"/>
    <circle cx="37" cy="37" r="20" fill="none" stroke="#111" stroke-width="2.5"/>
    <circle cx="37" cy="37" r="8" fill="none" stroke="#111" stroke-width="2.5"/>
    <path d="M37 2 V20 M37 54 V72 M2 37 H20 M54 37 H72" stroke="#111" stroke-width="2.5"/>
    <circle cx="37" cy="37" r="2.5" fill="#111"/>
  </svg>

  <section class="info-card info-card--services">
    <ul class="services">
      <li><svg class="tick" viewBox="0 0 20 20"><circle cx="10" cy="10" r="10" fill="var(--yellow)"/><path d="M5.5 10.3 L8.6 13.3 L14.6 6.8" fill="none" stroke="#111" stroke-width="2.2" stroke-linecap="round" stroke-linejoin="round"/></svg>Oil</li>
      <li><svg class="tick" viewBox="0 0 20 20"><circle cx="10" cy="10" r="10" fill="var(--yellow)"/><path d="M5.5 10.3 L8.6 13.3 L14.6 6.8" fill="none" stroke="#111" stroke-width="2.2" stroke-linecap="round" stroke-linejoin="round"/></svg>Braided</li>
      <li><svg class="tick" viewBox="0 0 20 20"><circle cx="10" cy="10" r="10" fill="var(--yellow)"/><path d="M5.5 10.3 L8.6 13.3 L14.6 6.8" fill="none" stroke="#111" stroke-width="2.2" stroke-linecap="round" stroke-linejoin="round"/></svg>Fuel</li>
      <li><svg class="tick" viewBox="0 0 20 20"><circle cx="10" cy="10" r="10" fill="var(--yellow)"/><path d="M5.5 10.3 L8.6 13.3 L14.6 6.8" fill="none" stroke="#111" stroke-width="2.2" stroke-linecap="round" stroke-linejoin="round"/></svg>Brake</li>
      <li class="wide"><svg class="tick" viewBox="0 0 20 20"><circle cx="10" cy="10" r="10" fill="var(--yellow)"/><path d="M5.5 10.3 L8.6 13.3 L14.6 6.8" fill="none" stroke="#111" stroke-width="2.2" stroke-linecap="round" stroke-linejoin="round"/></svg>Air Conditioning</li>
      <li class="wide"><svg class="tick" viewBox="0 0 20 20"><circle cx="10" cy="10" r="10" fill="var(--yellow)"/><path d="M5.5 10.3 L8.6 13.3 L14.6 6.8" fill="none" stroke="#111" stroke-width="2.2" stroke-linecap="round" stroke-linejoin="round"/></svg>Brake and fuel<br>pipes and fittings</li>
      <li class="wide"><svg class="tick" viewBox="0 0 20 20"><circle cx="10" cy="10" r="10" fill="var(--yellow)"/><path d="M5.5 10.3 L8.6 13.3 L14.6 6.8" fill="none" stroke="#111" stroke-width="2.2" stroke-linecap="round" stroke-linejoin="round"/></svg>Powersteering</li>
    </ul>
  </section>

  <ul class="contact contact--left">
    <li><svg class="icon" viewBox="0 0 20 20"><circle cx="10" cy="10" r="10" fill="var(--yellow)"/><path d="M10 4.5a3.6 3.6 0 0 0-3.6 3.6c0 2.7 3.6 7 3.6 7s3.6-4.3 3.6-7A3.6 3.6 0 0 0 10 4.5z" fill="none" stroke="#111" stroke-width="1.4"/><circle cx="10" cy="8.1" r="1.2" fill="#111"/></svg>18 Harbour View Road, Tauranga</li>
    <li><svg class="icon" viewBox="0 0 20 20"><circle cx="10" cy="10" r="10" fill="var(--yellow)"/><rect x="5" y="6.5" width="10" height="7" rx="1" fill="none" stroke="#111" stroke-width="1.4"/><path d="M5.3 7 L10 10.6 L14.7 7" fill="none" stroke="#111" stroke-width="1.4"/></svg>parts@kestrelmotorworks.co.nz</li>
    <li><svg class="icon" viewBox="0 0 20 20"><circle cx="10" cy="10" r="10" fill="var(--yellow)"/><circle cx="10" cy="10" r="5.2" fill="none" stroke="#111" stroke-width="1.3"/><ellipse cx="10" cy="10" rx="2.2" ry="5.2" fill="none" stroke="#111" stroke-width="1.1"/><path d="M4.8 10 H15.2" stroke="#111" stroke-width="1.1"/></svg>www.kestrelmotorworks.co.nz</li>
  </ul>

  <ul class="contact contact--right">
    <li><svg class="icon" viewBox="0 0 20 20"><circle cx="10" cy="10" r="10" fill="var(--yellow)"/><path d="M6.6 5.2l1.8-.4 1 2.5-1.2.9a6.4 6.4 0 0 0 3.5 3.5l.9-1.2 2.5 1-.4 1.8c-.2.6-.7.9-1.3.9A8.6 8.6 0 0 1 5.7 6.5c0-.6.3-1.1.9-1.3z" fill="#111"/></svg>Free Phone - 0800 55 41 82</li>
    <li class="no-icon">Ph 07 555 0142 | Fax 07 555 0143</li>
    <li class="unsubscribe">Unsubscribe from this list</li>
  </ul>
</main>
</body>
</html>
```